Tattoo Shop Business Card

I need a Business Card for the The Harbor Quill.

I'm thinking i want a double sided business card, really clean, very classy, one side the logo, and on the other my information. I'm pretty much open to anything, as long as its fun and captures class and elegance, while at the same time is edgy and tattooish.
I don't want your typical classic card. Add your own twist on it

Logo is attached to this brief

Please include:
Name
Position
Phone Number
Email
Website

Target Market(s)

I'm looking to capture potential clients for my tattoo shop so the card needs to be something they can fit in their wallet but they will also remember me when they see that card in there. My target audience is everyone over 18 that is intrigued by tattoos and piercings.

Industry/Entity Type

Business

Font styles to use
Serif

Colors

Designer to choose colors to be used in the design.

Requirements
Must have
• must be bold and something people will never forget

```html
<!DOCTYPE html>
<html lang="en">
<head>
<meta charset="utf-8">
<title>The Harbor Quill – Business Card</title>
<link rel="stylesheet" href="https://fonts.googleapis.com/css2?family=Libre+Baskerville:wght@400&display=swap">
<style>
  :root {
    --canvas: #e7e3dc;
    --card-dark: #2a2627;
    --card-dark-edge: #1f1c1d;
    --card-light: #f4f4f2;
    --ink-dark: #231f20;
    --ink-light: #f2f0ec;
    --ink-muted: #d6d2cd;
    --rule: #d9d9d6;
  }
  * { box-sizing: border-box; margin: 0; padding: 0; }
  html, body {
    width: 1200px;
    height: 886px;
    overflow: hidden;
    background: var(--canvas);
    font-family: "Libre Baskerville", Georgia, serif;
  }
  .canvas {
    position: relative;
    width: 1200px;
    height: 886px;
    display: flex;
    align-items: center;
    justify-content: center;
    gap: 40px;
  }
  .card {
    position: relative;
    width: 540px;
    height: 310px;
    border-radius: 16px;
    overflow: hidden;
    box-shadow: 0 10px 24px rgba(0,0,0,0.22);
  }

  /* Front: brand band over contact panel */
  .card-front { background: var(--card-dark); }
  .brand-band {
    position: absolute;
    inset: 0 0 auto 0;
    height: 150px;
    background: var(--card-light);
    border-bottom: 6px solid var(--rule);
    display: flex;
    align-items: center;
    justify-content: center;
  }
  .brand-name {
    font-size: 34px;
    font-weight: 400;
    letter-spacing: 1px;
    color: var(--ink-dark);
  }
  .contact-panel {
    position: absolute;
    left: 0; right: 0; bottom: 0;
    height: 160px;
    padding: 34px 40px 0 40px;
    display: flex;
    justify-content: space-between;
    color: var(--ink-light);
  }
  .person-name { font-size: 19px; line-height: 1.2; }
  .person-role { font-size: 13px; color: var(--ink-muted); margin-top: 4px; }
  .contact-list { list-style: none; font-size: 13px; line-height: 2; color: var(--ink-muted); text-align: left; }

  /* Back: brand on dark */
  .card-back {
    background: radial-gradient(ellipse at 45% 40%, #343031 0%, var(--card-dark) 55%, var(--card-dark-edge) 100%);
    display: flex;
    align-items: center;
    justify-content: center;
  }
  .card-back .brand-name { color: var(--ink-light); font-size: 36px; }
</style>
</head>
<body>
<main class="canvas">
  <section class="card card-front" aria-label="Business card front">
    <div class="brand-band">
      <h1 class="brand-name">The Harbor Quill</h1>
    </div>
    <div class="contact-panel">
      <div class="person">
        <p class="person-name">Employee Name</p>
        <p class="person-role">Managing Director</p>
      </div>
      <ul class="contact-list">
        <li>0012 3456 789</li>
        <li>info@youremail.com</li>
        <li>www.yourwebsite.com</li>
      </ul>
    </div>
  </section>

  <section class="card card-back" aria-label="Business card back">
    <p class="brand-name">The Harbor Quill</p>
  </section>
</main>
</body>
</html>
```